Package Design for Chew Bone Guild for Marketora

Would like a label to put on a 6x9 package.

Here is my site: chewboneguild.example

Here are the labels I like:
https://rolfandkit.example/collections/bully-sticks/products/6-inch-standard-bully-sticks
https://www.marketora.example/stores/Rolf+%26+Kit/page/A1B2C3D4-5E6F-47A8-9B0C-1D2E3F4A5B6C?ref_=ast_bln
https://quiet-meadowland.example/amber-hound-junior-bully-sticks-6-25-pack/
https://www.wagsandwhimsy.example/shop/open-trailer-bully-stix

```html
<!DOCTYPE html>
<html lang="en">
<head>
<meta charset="utf-8">
<title>Chew Bone Guild – Pouch Back Label</title>
<link rel="stylesheet" href="https://fonts.googleapis.com/css2?family=Baloo+2:wght@600;700;800&family=Nunito:wght@700&family=Lilita+One&display=swap">
<style>
  :root {
    --page-bg: #ececec;
    --sky-top: #8fc3ea;
    --sky-mid: #cfe5f7;
    --sky-low: #e4eff9;
    --grass-top: #86bf3a;
    --grass-low: #4f9d3a;
    --brown-deep: #5a2a1c;
    --brown-text: #4e2418;
    --rust: #a85a45;
    --cream: #fff6dd;
  }
  * { box-sizing: border-box; margin: 0; padding: 0; }
  html, body {
    width: 1200px; height: 1046px; overflow: hidden;
    background: var(--page-bg);
  }
  .pouch {
    position: absolute; left: 195px; top: 20px;
    width: 810px; height: 1006px;
    border-radius: 30px; overflow: hidden;
  }
  .sky-area {
    position: absolute; left: 0; top: 0; width: 100%; height: 700px;
    background: linear-gradient(180deg, var(--sky-top) 0%, var(--sky-mid) 35%, var(--sky-low) 100%);
  }
  .countryside-area {
    position: absolute; left: 0; top: 700px; width: 100%; height: 306px;
    background: linear-gradient(160deg, var(--grass-top) 0%, var(--grass-low) 100%);
  }
  .brand-mark {
    position: absolute; top: 108px; left: 0; width: 100%;
    display: flex; flex-direction: column; align-items: center; gap: 12px;
  }
  .brand-mark__dot {
    width: 120px; height: 120px; border-radius: 50%;
    background: var(--cream);
  }
  .brand-mark__name {
    font-family: "Baloo 2", sans-serif; font-weight: 800;
    font-size: 36px; line-height: 1; letter-spacing: 1px;
    color: var(--brown-deep); text-transform: uppercase;
  }
  .product-story {
    position: absolute; top: 366px; left: 80px; width: 650px;
    font-family: "Nunito", sans-serif; font-weight: 700;
    font-size: 16px; line-height: 19px; text-align: center;
    color: var(--brown-text);
  }
  .benefits {
    position: absolute; top: 588px; left: 0; width: 100%;
    display: grid; grid-template-columns: 1fr 3px 1fr; column-gap: 22px;
    font-family: "Baloo 2", sans-serif; font-weight: 700;
    font-size: 23px; line-height: 33px; color: var(--rust);
    text-transform: uppercase;
  }
  .benefits__col { list-style: none; }
  .benefits__col--left { text-align: right; }
  .benefits__divider { background: var(--rust); border-radius: 2px; }
  .signoff {
    position: absolute; top: 804px; left: 0; width: 100%; text-align: center;
  }
  .signoff__name {
    font-family: "Lilita One", sans-serif; font-size: 48px; line-height: 1;
    color: var(--brown-deep); text-transform: uppercase; letter-spacing: 0.5px;
  }
  .signoff__tagline {
    margin-top: 14px;
    font-family: "Lilita One", sans-serif; font-size: 31px; line-height: 1;
    color: var(--brown-deep); text-transform: uppercase;
  }
</style>
</head>
<body>
  <main class="pouch">
    <div class="sky-area" role="img" aria-label="Illustrated sunny blue sky with soft clouds and light rays"></div>
    <div class="countryside-area" role="img" aria-label="Illustrated green rolling hills with a winding path, trees and a ribbon banner behind the tagline"></div>

    <header class="brand-mark">
      <span class="brand-mark__dot"></span>
      <span class="brand-mark__name">Chew Bone Guild</span>
    </header>

    <p class="product-story">
      Our bully sticks are sourced from grass fed, free range cattle; raised without any added hormones or antibiotics, resulting in a healthier and better tasting treat. Processed in a USDA Human Grade Certified and Inspected facility. Each bully stick is six inches and 8-14 gm each; they're handpicked and inspected to ensure quality, texture and perfect consistency.<br>
      100% Guaranteed to be fully digestible and guaranteed not to cause any side-effects. Bully Sticks are a natural, low-fat and protein-rich, one-ingredient dog chew treat, being 100% beef muscle without any additives or artificial ingredients.
    </p>

    <section class="benefits">
      <ul class="benefits__col benefits__col--left">
        <li>Low in fat</li>
        <li>Chemical free</li>
        <li>Provides stress relief</li>
      </ul>
      <span class="benefits__divider"></span>
      <ul class="benefits__col">
        <li>100% digestible</li>
        <li>High in protein</li>
        <li>Promotes oral health</li>
      </ul>
    </section>

    <footer class="signoff">
      <h1 class="signoff__name">Chew Bone Guild</h1>
      <p class="signoff__tagline">Your dog will bag for more!</p>
    </footer>
  </main>
</body>
</html>
```